Box design for “lunchbox”

Environmental box for adults and children. I need a design for a carton packing .

details:

measurement;
L: 17 cm
W: 24 cm
D:9 cm

*NO logo, only the font i have mentioned down
*need full design from each side

the information that should be mentioned on the box is:

>Protected by: [login to view URL]

>Product space:
-Approx:
-Weight:
-Dimensions:
-Materials: Stainless steel , silicone rubber

>Cleaning Tips:
-Wash your KALIRAP hand wash. Dry after washing
-hand wash your carry bag regularly
- you can fully submerge in water and soap

>Made in china

The website that should be on the design is; [login to view URL]
The brand name is; kalirap
The font of the logo you can find on this link; [login to view URL]

And there’s some pictures may help you.

```html
<!DOCTYPE html>
<html lang="en">
<head>
<meta charset="utf-8">
<title>KALIRAP Lunchbox Carton Dieline</title>
<link rel="stylesheet" href="https://fonts.googleapis.com/css2?family=Josefin+Sans:wght@300;400&family=Roboto:wght@400&display=swap">
<style>
  :root {
    --page: #ffffff;
    --kraft: #c99c66;
    --cut: #6e6a66;
    --fold: #f19ad3;
    --ink: #1d1915;
    --label: #1a1a1a;
  }
  html, body {
    margin: 0;
    padding: 0;
    width: 1200px;
    height: 849px;
    overflow: hidden;
    background: var(--page);
  }
  .dieline {
    display: block;
    width: 1200px;
    height: 849px;
  }
  .panel { fill: var(--kraft); stroke: var(--cut); stroke-width: 2; }
  .fold-line { stroke: var(--fold); stroke-width: 1.6; fill: none; }
  .leader { stroke: var(--fold); stroke-width: 1.6; }
  .box-text { fill: var(--ink); font-family: "Josefin Sans", sans-serif; font-weight: 400; }
  .brand-front { font-size: 62px; font-weight: 300; letter-spacing: 2px; }
  .brand-small { font-size: 15px; font-weight: 300; letter-spacing: 1px; }
  .tagline { font-size: 19px; font-weight: 300; letter-spacing: 0.5px; }
  .spec { font-size: 10px; }
  .tip { font-size: 7.5px; letter-spacing: 0.2px; }
  .tips-title { font-size: 15px; font-weight: 300; letter-spacing: 1px; }
  .side-note { font-size: 9.5px; letter-spacing: 0.6px; }
  .annotation { fill: var(--label); font-family: "Roboto", Arial, sans-serif; font-size: 14px; }
  .divider { stroke: var(--ink); stroke-width: 1.4; }
  .slot { stroke: var(--cut); stroke-width: 1.6; fill: none; }
  .swatch { fill: #000000; }
</style>
</head>
<body>
<svg class="dieline" viewBox="0 0 1200 849" xmlns="http://www.w3.org/2000/svg">

  <!-- Side 4 flap -->
  <path class="panel" d="M287,141 V60 L296,49 H517 A17,17 0 0 0 551,49 H771 L779,60 V141 Z"/>

  <!-- Middle row: side 1, back, side 3 -->
  <rect class="panel" x="154" y="141" width="802" height="245"/>

  <!-- Side 2 row with dust flaps -->
  <path class="panel" d="M291,390 H374 V476 H291 Q287,476 287,472 V394 Q287,390 291,390 Z"/>
  <rect class="panel" x="377" y="386" width="353" height="94"/>
  <path class="panel" d="M733,390 H776 Q780,390 780,394 V472 Q780,476 776,476 H733 Z"/>

  <!-- Front with tuck flap -->
  <path class="panel" d="M342,480 H765 Q779,480 779,494 V690 Q779,712 760,718 L735,727 L728,780 Q726,791 715,791 H393 Q382,791 380,780 L373,727 L348,718 Q328,712 328,690 V494 Q328,480 342,480 Z"/>
  <path class="slot" d="M522,762 L527,756 H581 L586,762"/>

  <!-- Fold lines -->
  <g class="fold-line">
    <line x1="377" y1="49" x2="377" y2="727"/>
    <line x1="730" y1="49" x2="730" y2="727"/>
    <line x1="287" y1="103" x2="779" y2="103"/>
    <line x1="287" y1="141" x2="779" y2="141"/>
    <line x1="188" y1="141" x2="188" y2="386"/>
    <line x1="287" y1="141" x2="287" y2="386"/>
    <line x1="826" y1="141" x2="826" y2="386"/>
    <line x1="921" y1="141" x2="921" y2="386"/>
    <line x1="377" y1="386" x2="730" y2="386"/>
    <line x1="377" y1="480" x2="730" y2="480"/>
    <line x1="377" y1="727" x2="730" y2="727"/>
  </g>

  <!-- Side 1 -->
  <g class="box-text side-note" transform="rotate(90 322 258)">
    <text x="322" y="254" text-anchor="middle">PROTECTED BY</text>
    <text x="322" y="268" text-anchor="middle">WWW.KALIRAP.COM</text>
  </g>
  <g class="recycle-icon" transform="translate(297 370)" fill="none" stroke="var(--ink)" stroke-width="1.8">
    <path d="M-6,3 L0,-7 L6,3 Z"/>
  </g>

  <!-- Back: upside-down care copy -->
  <g class="back-copy box-text" transform="rotate(180 553 262)">
    <text class="tips-title" x="541" y="213" text-anchor="middle">CLEANING TIPS</text>
    <rect role="img" aria-label="Small sparkle accents" x="610" y="184" width="16" height="17" fill="var(--ink)" opacity="0.85"/>
    <text class="tip" x="553" y="274" text-anchor="middle" textLength="178" lengthAdjust="spacingAndGlyphs">- WASH YOUR KALIRAP HAND WASH. DRY AFTER WASHING</text>
    <text class="tip" x="553" y="295" text-anchor="middle" textLength="150" lengthAdjust="spacingAndGlyphs">- HAND WASH YOUR CARRY BAG REGULARLY</text>
    <text class="tip" x="553" y="312" text-anchor="middle" textLength="170" lengthAdjust="spacingAndGlyphs">- YOU CAN FULLY SUBMERGE IN WATER AND SOAP</text>
    <text class="tip" x="553" y="336" text-anchor="middle">POWERED BY</text>
    <text class="tip" x="553" y="348" text-anchor="middle">WWW.KALIRAP.COM</text>
  </g>

  <!-- Side 3 -->
  <g class="box-text tagline" transform="rotate(-90 785 262)">
    <text x="785" y="251" text-anchor="middle">WHEN YOU THINK LUNCH.</text>
    <text x="785" y="279" text-anchor="middle">THINK KALIRAP</text>
  </g>

  <!-- Side 2: product specs -->
  <text class="box-text brand-small" x="440" y="441" text-anchor="middle">KALIRAP</text>
  <line class="divider" x1="494" y1="400" x2="494" y2="468"/>
  <g class="box-text spec">
    <text x="520" y="410">PRODUCT SPECS:</text>
    <text x="520" y="424">-APPROX:</text>
    <text x="520" y="438">-WEIGHT:</text>
    <text x="520" y="452">-DIMENSIONS:</text>
    <text x="520" y="467" textLength="194" lengthAdjust="spacingAndGlyphs">-MATERIALS: STAINLESS STEEL, SILICONE RUBBER</text>
  </g>

  <!-- Front -->
  <text class="box-text brand-front" x="553" y="637" text-anchor="middle">KALIRAP</text>

  <!-- Panel callouts -->
  <g class="callouts">
    <line class="leader" x1="730" y1="103" x2="1002" y2="220"/>
    <text class="annotation" x="1007" y="238">SIDE 4</text>
    <line class="leader" x1="290" y1="346" x2="103" y2="425"/>
    <text class="annotation" x="73" y="447">SIDE 1</text>
    <line class="leader" x1="826" y1="370" x2="955" y2="420"/>
    <text class="annotation" x="960" y="433">SIDE 3</text>
    <line class="leader" x1="678" y1="346" x2="955" y2="473"/>
    <text class="annotation" x="960" y="486">BACK</text>
    <line class="leader" x1="734" y1="480" x2="862" y2="531"/>
    <text class="annotation" x="867" y="542">SIDE 2</text>
    <line class="leader" x1="720" y1="621" x2="914" y2="708"/>
    <text class="annotation" x="919" y="720">FRONT</text>
  </g>

  <!-- Dimensions -->
  <g class="annotation dimensions">
    <text x="42" y="741">L: 17 cm</text>
    <text x="42" y="773">W: 24 cm</text>
    <text x="42" y="804">D: 9 cm</text>
  </g>

  <!-- Colour reference -->
  <text class="annotation" x="1030" y="740">COLOR REFERENCE</text>
  <rect class="swatch" x="1073" y="756" width="52" height="52"/>
</svg>
</body>
</html>
```